New Wanderly Site!!

Hello everyone!
We're WanderlyTrips. A tour company which offer group excursions to places like Morocco & Portugal for young adults. We have been in the business for 10 years now and we'd like to create a new fresh look and feel design. Something clean and more modern.
We offer trips to:
1 - Weekend trips Lagos, Portugal
2 - Weekend tips to Morocco
3 - 5 day trip to the Sahara Desert in Morocco
4 - Beach day trips to Cadiz
5 - Day trip to Gibraltar
6 - Costume trips
7 - Wine Tasting day trip
8 - Fiestas del Torvell
Those are the 8 boxes we'd like to have on our home-page along with an awesome header and footer. You can take a look for our current page to see sections and the text of the sections. Once we approve a nice home page from any of you designers, we will go ahead and send you the names of all the pages we'd like you to design for us. We already have someone who will code all the pages. We just need a new design for all the pages.
You can see our logo on our Blog: http://wanderlytripsblog.example/
We like websites like:
www.Palorvia.example
www.Skarmet.example
We look forward to hear from you!!
PS:
we will need the home page and other pages.
7 pages plus 8 trip pages. The trip pages they can all look the same (design wise) obviusly diferent photos, video and content. Total 15 pages.
Page 1 - Home page
Page 2 - About us. This page can look similar to:
Page 3 - FAQs. This page can look similar to:
Page 4 - Contact us. This page can look similar to: http://www.palorvia.example/contact
Page 5 - Trip check in. This page can look similar to the Skarmet.example look for flight check in. Something clean.
Page 6 - Trip videos. This page, will have the list of all our trip videos. A line or two of the trip and the video right below.
Page 7 - Trip departure info. On this page we're going to have the information on how to get to Sevilla. Also the google map of the actual meeting point and maybe a youtube video somewhere.
Page 8 - Why travel with us.
How many trip page are we going to need?
We have 8 trips. If you can just do 1 page, then you can do the same type page for all the trips. On each trip page you must add the following content:
Trip overview
Whats included
Trip dates
Photos and a youtube video.
An example of our current lagos trip page is:
https://www.wanderlytrips.example/2001/09/beach-getaway-lagos-portugal/
You can take all the content from www.WanderlyTrips.example

```html
<!DOCTYPE html>
<html lang="en">
<head>
<meta charset="utf-8">
<title>WanderlyTrips – Contact</title>
<link rel="stylesheet" href="https://fonts.googleapis.com/css2?family=Source+Sans+3:wght@400;600;700&display=swap">
<style>
:root{
  --brand-red:#a30f12;
  --btn-red:#b3161b;
  --ink:#1e1e1e;
  --muted:#444;
  --form-gold:#fdb100;
  --footer:#3d3d3d;
  --footer-base:#2f2f2f;
  --footer-text:#e6e6e6;
  --page-bg:#f1f1f1;
  --topbar:#ececec;
}
*{box-sizing:border-box;margin:0;padding:0}
html,body{width:883px;height:1200px;overflow:hidden}
body{font-family:"Source Sans 3",Arial,sans-serif;background:var(--page-bg);color:var(--ink);position:relative}
.site-header{position:absolute;top:0;left:0;width:883px;height:90px;background:#fff;border-top:2px solid #3a0b0b}
.brand{position:absolute;left:74px;top:34px;display:flex;align-items:center;gap:7px;font-weight:700;font-size:20px;color:var(--ink)}
.brand-dot{width:12px;height:12px;border-radius:50%;background:var(--brand-red)}
.utility-nav{position:absolute;left:534px;top:0;width:274px;height:33px;background:var(--topbar);display:flex;align-items:center;justify-content:center;font-size:10.5px;color:#333}
.utility-nav span.sep{margin:0 6px;color:#666}
.main-nav{position:absolute;right:75px;top:60px;display:flex;gap:20px;font-weight:700;font-size:13px;color:var(--brand-red)}
.hero{position:absolute;top:90px;left:0;width:883px;height:238px;background:linear-gradient(180deg,#a9c3e6 0%,#4f8fd0 30%,#3aa7d6 55%,#5fd0e3 75%,#3f9ac9 100%)}
.content{position:absolute;top:328px;left:56px;width:771px;height:627px;background:#fff}
.contact-info{position:absolute;left:36px;top:26px;width:600px}
.contact-info h1{font-size:21px;font-weight:600;color:var(--brand-red);margin-bottom:12px}
.contact-info .primary{font-size:12.5px;line-height:18px}
.contact-info .primary b{font-weight:400;font-size:10.5px}
.contact-info .small{font-size:9.5px;line-height:14px;color:var(--muted);margin-top:8px}
.contact-form{position:absolute;left:33px;top:189px;width:473px;height:371px;background:var(--form-gold);border:1px solid #c98900;border-radius:6px;overflow:hidden}
.form-head{height:40px;background:#000;color:#fff;font-size:15.5px;font-weight:600;padding:12px 22px 0}
.field-label{position:absolute;font-size:11px;color:#2a2a2a}
.input{position:absolute;height:22px;background:#fff;border:1px solid #e0a000;border-radius:2px}
.select{font-size:9px;color:#888;padding:5px 8px}
.select svg{position:absolute;right:7px;top:8px}
.btn-send{position:absolute;left:30px;top:312px;width:127px;height:30px;background:var(--btn-red);color:#fff;font-size:12px;font-weight:600;border:1px solid #7a0a0c;border-radius:3px;display:flex;align-items:center;justify-content:center}
.travel-icons svg{position:absolute;fill:#3d3d3d}
.site-footer{position:absolute;top:954px;left:0;width:883px;height:190px;background:var(--footer);color:var(--footer-text)}
.footer-col{position:absolute;top:34px}
.footer-col h3{font-size:15px;font-weight:400;margin-bottom:7px;color:#fff}
.footer-col li{list-style:none;font-size:10px;line-height:18px}
.divider{position:absolute;top:38px;width:1px;height:108px;background:#555}
.footer-base{position:absolute;top:1144px;left:0;width:883px;height:56px;background:var(--footer-base);color:#bbb;font-size:9px;padding:22px 75px}
</style>
</head>
<body>
<header class="site-header">
  <div class="brand"><span class="brand-dot"></span>WanderlyTrips</div>
  <nav class="utility-nav">Register<span class="sep">|</span>Sign In<span class="sep">|</span>Newsletters<span class="sep">|</span>Support<span class="sep">|</span>Contact</nav>
  <nav class="main-nav"><span>HOME</span><span>TOURS</span><span>WHO WE ARE</span><span>LATEST DEALS</span><span>BOOK NOW</span><span>SPECIAL OFFERS</span><span>RESOUCES</span></nav>
</header>

<div class="hero" role="img" aria-label="Aerial view of a tropical island with turquoise lagoon and green islets"></div>

<main class="content">
  <section class="contact-info">
    <h1>Contact Information</h1>
    <p class="primary"><b>Email:</b> info@wanderlytrips.example</p>
    <p class="primary">Phone: +34 900 11 47 58</p>
    <p class="small">Address: Calle Almendro Rojo, 14 41001 Sevilla, España</p>
    <p class="small">Office: Our office is located in beautiful Sevilla. Please feel free to stop by if you are in the area! Our great team will be more than happy to help you. We are open from Mondays to Fridays from 10.00Am to 8.00PM (no siesta in between!)</p>
  </section>

  <form class="contact-form">
    <div class="form-head">Fill Our Contact Form here</div>
    <span class="field-label" style="left:29px;top:54px">First Name</span>
    <div class="input" style="left:29px;top:69px;width:175px"></div>
    <div class="input" style="left:217px;top:69px;width:175px"></div>
    <span class="field-label" style="left:29px;top:102px">Email addresss</span>
    <span class="field-label" style="left:217px;top:102px">Phone no.</span>
    <div class="input" style="left:29px;top:117px;width:175px"></div>
    <div class="input" style="left:217px;top:117px;width:175px"></div>
    <span class="field-label" style="left:29px;top:146px">City/State</span>
    <div class="input select" style="left:29px;top:161px;width:175px">Please Select
      <svg width="9" height="6" viewBox="0 0 9 6"><path d="M0 0h9L4.5 6z" fill="#666"/></svg>
    </div>
    <span class="field-label" style="left:30px;top:197px">Message/Comment</span>
    <div class="input" style="left:30px;top:215px;width:367px;height:89px"></div>
    <div class="btn-send">Send Your Messsage</div>
  </form>

  <div class="travel-icons">
    <svg style="left:40px;top:612px" width="32" height="15" viewBox="0 0 32 15"><path d="M2 9h26c3 0 4 2 2 3H8z M10 9 4 1h4l9 8z M12 12l-4 3h4l6-3z"/></svg>
    <svg style="left:470px;top:604px" width="62" height="23" viewBox="0 0 62 23"><path d="M0 14h58l-8 9H6z M14 14l6-8h24l8 8z M30 6l4-5h8l-4 5z"/></svg>
    <svg style="left:718px;top:602px" width="30" height="25" viewBox="0 0 30 25"><path d="M14 6h2v15h-2z M15 6C10 0 4 2 2 6c4-2 8-2 13 0zM15 6c5-6 11-4 13 0-4-2-8-2-13 0z M3 25c3-6 21-6 24 0z"/></svg>
  </div>
</main>

<footer class="site-footer">
  <div class="footer-col" style="left:74px"><h3>Company</h3><ul><li>Ou Mission</li><li>Why Choose Us</li><li>Testimonials</li><li>Recent Blog Posts</li><li>Newsletters</li></ul></div>
  <span class="divider" style="left:181px"></span>
  <div class="footer-col" style="left:219px"><h3>Book Your Tours</h3><ul><li>Find Your Tour</li><li>Book Now</li><li>Why Choose Us</li><li>Latest Offers</li><li>Best Tours</li></ul></div>
  <span class="divider" style="left:347px"></span>
  <div class="footer-col" style="left:379px"><h3>Your Booking</h3><ul><li>My Reservation</li><li>Check-in online</li><li>Change your flight</li><li>Lock your price</li></ul></div>
  <span class="divider" style="left:492px"></span>
  <div class="footer-col" style="left:526px"><h3>Customer Support</h3><ul><li>Our Support</li><li>Enquiry Now</li><li>Chat Now</li><li>FAQ's</li><li>Term &amp; Use</li></ul></div>
  <span class="divider" style="left:666px"></span>
  <div class="footer-col" style="left:691px"><h3>Get Connected</h3></div>
</footer>
<div class="footer-base">© 2012 Company Name.&nbsp; All right reserved.&nbsp; Term of Use</div>
</body>
</html>
```